Postcard for commercial concrete cleaning company that will be mailed to business customers

A 6x9 postcard that will be mailed out to businesses who have concrete (sidewalks, drive thrus, dumpster pads, etc) that need periodic pressure washing to keep clean. Our current customers are majority restaurants. We are able to remove gum and grease from concrete which is difficult for much of our competitors. We work at night when the businesses are closed or slow if 24hr.

Target Market(s)

This will go to restaurants, banks, gas stations and other retail locations.

Colors

Designer to choose colors to be used in the design.

Requirements
Must have
• Logo. A headline that mentions commercial concrete cleaning so recipients will know at a glance what we do
Nice to have
• The image included is of a fast food doorway that is half cleaned, the right side. Something like "Dirty Doorway?" may make sense.
• We specialize is maintenance concrete cleaning where we come on a regular basis so I like phrase keep your concrete clean, or keep your business clean. something like that.

```html
<!DOCTYPE html>
<html lang="en">
<head>
<meta charset="utf-8">
<title>Keystone Commercial Pressure Washing – Postcard</title>
<link href="https://fonts.googleapis.com/css2?family=Lato:wght@400;700;900&display=swap" rel="stylesheet">
<style>
  :root{
    --page:#e6e7e9;
    --card:#ffffff;
    --card-sheen:#eceef1;
    --brand-blue:#1b6cb7;
    --navy:#1d2a5c;
    --ink:#2f3136;
    --rule:#3a3c40;
    --stamp:#3b3c3f;
    --white:#ffffff;
  }
  *{box-sizing:border-box;margin:0;padding:0}
  html,body{width:1200px;height:471px;overflow:hidden}
  body{background:var(--page);font-family:"Lato",Arial,sans-serif;position:relative}
  .card{position:absolute;top:54px;width:548px;height:364px;overflow:hidden;
    background:linear-gradient(120deg,var(--card) 0%,var(--card) 45%,var(--card-sheen) 60%,var(--card) 72%,var(--card-sheen) 100%)}
  .card--front{left:44px}
  .card--back{left:608px}

  .brand{position:absolute;color:var(--navy);font-weight:700;line-height:1.05;text-align:center}
  .brand__name{font-size:27px;display:block}
  .brand__trade{font-size:20px;letter-spacing:4px;display:block;margin-top:4px}
  .card--front .brand{left:0;right:0;top:30px}
  .card--back .brand{left:28px;top:34px;text-align:left}

  .photo{position:absolute;border:3px solid var(--white)}
  .photo--deck{left:14px;top:125px;width:130px;height:103px;background:linear-gradient(135deg,#5d4a3c,#8a5a35 60%,#b07848)}
  .photo--doorway{left:142px;top:106px;width:266px;height:139px;background:linear-gradient(180deg,#8d8a80 0%,#b4aa97 40%,#9f9a8d 70%,#d0c6b0 100%)}
  .photo--steps{left:406px;top:125px;width:130px;height:103px;background:linear-gradient(160deg,#5e4a3e,#a24a37 45%,#c0553d 80%,#8f3f30)}
  .tag{position:absolute;left:200px;top:222px;width:148px;height:22px;background:var(--brand-blue);color:var(--white);
    font-weight:700;font-size:13px;line-height:22px;text-align:center;letter-spacing:.3px;
    clip-path:polygon(8px 0,calc(100% - 8px) 0,100% 100%,0 100%)}

  .headline{position:absolute;left:0;right:0;top:252px;text-align:center;color:var(--brand-blue);font-weight:900;font-size:32px;letter-spacing:-.2px}
  .tagline{position:absolute;left:40px;right:40px;top:294px;display:flex;align-items:center;gap:14px;
    font-weight:700;font-size:12.5px;color:var(--ink)}
  .tagline::before,.tagline::after{content:"";flex:1;height:3px;background:var(--rule)}
  .contact-band{position:absolute;left:0;right:0;bottom:0;height:46px;background:var(--brand-blue);color:var(--white);
    font-weight:700;font-size:16px;line-height:46px;text-align:center}

  .stamp{position:absolute;left:464px;top:22px;width:61px;height:60px;background:var(--stamp)}
  .services{position:absolute;left:28px;top:112px;font-size:13px;font-weight:700;color:var(--ink)}
  .pitch{position:absolute;left:0;top:140px;width:324px;height:123px;background:var(--brand-blue);color:var(--white);
    clip-path:polygon(0 0,100% 0,calc(100% - 24px) 100%,0 100%);padding:12px 40px 0 26px;font-size:12.6px;line-height:1.35}
  .pitch p+p{margin-top:13px}
  .back-address{position:absolute;left:28px;top:279px;font-size:14px;color:var(--ink)}
  .back-phone{position:absolute;left:28px;top:297px;font-size:30px;font-weight:900;color:var(--ink)}
  .address-lines{position:absolute;left:348px;top:204px;width:177px}
  .address-lines span{display:block;height:1px;background:var(--rule);margin-bottom:37px}
</style>
</head>
<body>
  <section class="card card--front">
    <div class="brand"><span class="brand__name">Keystone Commercial</span><span class="brand__trade">PRESSURE WASHING</span></div>
    <div class="photo photo--deck" role="img" aria-label="Wooden deck being cleaned with a pressure washer wand"></div>
    <div class="photo photo--steps" role="img" aria-label="Red brick steps, half cleaned"></div>
    <div class="photo photo--doorway" role="img" aria-label="Restaurant doorway concrete, right half pressure washed clean"></div>
    <div class="tag">DIRTY DOORWAY?</div>
    <h1 class="headline">Commercial Concrete Cleaning</h1>
    <div class="tagline">Periodic Pressure Washing To Keep Clean</div>
    <div class="contact-band">48 Alder Row Ct, Fairhaven, TN 37000 | Ph: (555) 010-2468</div>
  </section>

  <section class="card card--back">
    <div class="brand"><span class="brand__name">Keystone Commercial</span><span class="brand__trade">PRESSURE WASHING</span></div>
    <div class="stamp"></div>
    <div class="services">Sidewalks | Drive Thrus | Dumpster Pads, Etc</div>
    <div class="pitch">
      <p>We are able to remove gum and grease from concrete which is difficult for much of our competitors.</p>
      <p>We work at night when the businesses are closed or slow if 24hr.</p>
    </div>
    <div class="address-lines"><span></span><span></span><span></span></div>
    <div class="back-address">48 Alder Row Ct, Fairhaven, TN 37000</div>
    <div class="back-phone">Ph: (555) 010-2468</div>
  </section>
</body>
</html>
```